I would like to design a flyer that I can put on car windows, inside peoples mailboxes. This flyer is to display Vantor Athletics and Wellness is now Open. I would like this to be a Free One Week Pass! I would like to have the following information on the flyer.
1) My logo - VANTOR ATHLETICS AND WELLNESS (I will upload the logo)
2) Hours of operation - Mon - Fri "5am - 10pm" Sat/Sun "6am -6pm"
3) Membership $59.00 "No Initiation Fee" Month to Month Membership.
Class are free. The Classes are Yoga, Salsa Classes, Bootcamps, HITT, Sports Performance,
4) Personal Training
5) Message Therapy
6) Address: 2718 Marwick Commerce Dr. Suite 312
Chantilly, VA 20987
7) mail@vantoranw.example
8) Free One Week Pass

```html
<!DOCTYPE html>
<html lang="en">
<head>
<meta charset="utf-8">
<title>Vantor Athletics and Wellness – Free One Week Pass</title>
<link href="https://fonts.googleapis.com/css2?family=Open+Sans:ital,wght@0,400;0,600;0,700;1,400&display=swap" rel="stylesheet">
<style>
  :root {
    --red: #e2231a;
    --dark: #3b3b3c;
    --ink: #333333;
    --paper: #f4f4f4;
    --stripe: #e3e3e3;
    --backdrop: #ffffff;
    --white: #ffffff;
  }
  * { box-sizing: border-box; margin: 0; padding: 0; }
  html, body {
    width: 1200px; height: 1200px; overflow: hidden;
    background: var(--backdrop);
    font-family: "Open Sans", Arial, sans-serif;
  }
  .flyer {
    position: absolute; left: 190px; top: 20px;
    width: 820px; height: 1160px;
    background: var(--paper);
    overflow: hidden;
    box-shadow: 0 6px 24px rgba(0,0,0,.18);
  }
  .flyer-art { position: absolute; inset: 0; }
  .pass-band {
    position: absolute; left: 40px; top: 418px;
    width: 520px; height: 56px;
    color: var(--white); font-size: 41px; font-weight: 400;
    letter-spacing: .5px; padding-left: 22px; line-height: 56px;
  }
  .services {
    position: absolute; left: 40px; top: 490px;
    color: var(--white); font-size: 20px; letter-spacing: .5px;
    display: flex; gap: 26px;
  }
  .services span::before {
    content: "\2713"; color: var(--red); font-weight: 700; margin-right: 4px;
  }
  .badge {
    position: absolute; left: 590px; top: 130px; width: 200px; height: 200px;
    color: var(--white); text-align: center; text-transform: uppercase;
    display: flex; flex-direction: column; justify-content: center;
  }
  .badge-label { font-size: 16px; font-weight: 600; }
  .badge-price { font-size: 62px; font-weight: 700; line-height: 1; }
  .badge-note { font-size: 19px; font-weight: 600; line-height: 1.2; margin-top: 4px; }
  .schedule {
    position: absolute; left: 60px; top: 870px; color: var(--ink);
  }
  .schedule h2 {
    color: var(--red); font-size: 29px; font-weight: 600; margin-bottom: 2px;
  }
  .schedule p { font-size: 21px; font-style: italic; line-height: 1.3; }
  .classes {
    position: absolute; right: 90px; top: 852px;
    text-align: right; color: var(--ink); font-size: 18px; line-height: 1.3;
  }
  .brand {
    position: absolute; right: 80px; top: 995px;
    display: flex; align-items: center; gap: 12px;
  }
  .brand-dot {
    width: 48px; height: 48px; border-radius: 50%; background: var(--red);
  }
  .brand-name {
    color: var(--red); font-size: 22px; font-weight: 600; letter-spacing: .5px;
  }
  .footer {
    position: absolute; left: 0; bottom: 0; width: 100%; height: 100px;
    background: var(--dark); color: var(--white);
    text-align: center; font-size: 15px; font-weight: 600; line-height: 1.45;
    padding-top: 20px;
  }
</style>
</head>
<body>
<main class="flyer">
  <svg class="flyer-art" width="820" height="1160" viewBox="0 0 820 1160">
    <defs>
      <pattern id="diagonal-stripes" width="34" height="34" patternUnits="userSpaceOnUse" patternTransform="rotate(35)">
        <rect width="14" height="34" fill="var(--stripe)"/>
      </pattern>
      <clipPath id="hero-clip"><circle cx="300" cy="300" r="470"/></clipPath>
      <linearGradient id="hero-tones" x1="0" y1="0" x2="0.3" y2="1">
        <stop offset="0" stop-color="#8a6a5a"/>
        <stop offset="0.55" stop-color="#6e625c"/>
        <stop offset="1" stop-color="#8c938c"/>
      </linearGradient>
      <linearGradient id="park-tones" x1="0" y1="0" x2="0" y2="1">
        <stop offset="0" stop-color="#7fae4a"/><stop offset="1" stop-color="#4f8f2e"/>
      </linearGradient>
      <linearGradient id="yoga-tones" x1="0" y1="0" x2="0" y2="1">
        <stop offset="0" stop-color="#b8a89c"/><stop offset="1" stop-color="#8f7f80"/>
      </linearGradient>
      <radialGradient id="dance-tones"><stop offset="0" stop-color="#e39a3c"/><stop offset="1" stop-color="#b8661c"/></radialGradient>
    </defs>

    <rect x="500" y="0" width="320" height="560" fill="url(#diagonal-stripes)"/>

    <g role="img" aria-label="Photo: two women lifting hand weights in a brick-walled studio">
      <rect width="820" height="1160" fill="url(#hero-tones)" clip-path="url(#hero-clip)"/>
    </g>

    <path d="M 0 700 A 480 480 0 0 0 300 780 L 360 776" fill="none" stroke="var(--red)" stroke-width="10"/>
    <path d="M 0 735 A 500 500 0 0 0 300 800" fill="none" stroke="#9a9a9a" stroke-width="5"/>
    <path d="M 330 772 A 470 470 0 0 0 700 520" fill="none" stroke="var(--red)" stroke-width="6"/>

    <rect x="40" y="418" width="540" height="56" fill="rgba(60,60,60,.78)"/>
    <line x1="60" y1="478" x2="250" y2="478" stroke="var(--white)" stroke-width="3"/>
    <line x1="250" y1="478" x2="580" y2="478" stroke="var(--red)" stroke-width="3"/>

    <circle cx="690" cy="230" r="104" fill="var(--red)"/>
    <circle cx="690" cy="230" r="92" fill="none" stroke="var(--white)" stroke-width="3"/>

    <g role="img" aria-label="Photo: outdoor bootcamp group doing squats on grass">
      <circle cx="690" cy="560" r="66" fill="url(#park-tones)" stroke="var(--white)" stroke-width="7"/>
    </g>
    <g role="img" aria-label="Photo: women sitting in yoga meditation pose">
      <circle cx="570" cy="705" r="66" fill="url(#yoga-tones)" stroke="var(--white)" stroke-width="7"/>
    </g>
    <g role="img" aria-label="Photo: salsa dancing couple">
      <circle cx="450" cy="835" r="66" fill="url(#dance-tones)" stroke="var(--white)" stroke-width="7"/>
    </g>

    <rect x="760" y="880" width="18" height="120" fill="var(--red)"/>
    <rect x="788" y="850" width="32" height="80" fill="var(--red)"/>
    <rect x="800" y="940" width="20" height="110" fill="var(--red)"/>
  </svg>

  <div class="badge">
    <span class="badge-label">Membership</span>
    <span class="badge-price">$59</span>
    <span class="badge-note">"No<br>Initiation<br>Fee"</span>
  </div>

  <h1 class="pass-band">FREE ONE WEEK PASS</h1>
  <div class="services">
    <span>PERSONAL TRAINING</span>
    <span>MESSAGE THERAPY</span>
  </div>

  <section class="schedule">
    <h2>TIME SCHEDULE</h2>
    <p>MON - FRI<br>"5AM - 10PM"<br>SAT/SUN<br>"6AM -6PM"</p>
  </section>

  <section class="classes">
    Class are free.<br>
    The Classes are Yoga<br>
    Salsa Classes<br>
    Bootcamps<br>
    HITT<br>
    Sports Performance
  </section>

  <div class="brand">
    <span class="brand-dot"></span>
    <span class="brand-name">VANTOR ATHLETICS AND WELLNESS</span>
  </div>

  <footer class="footer">
    Address: 2718 Marwick Commerce Dr. Suite 312<br>
    Chantilly, VA 20987<br>
    mail@vantoranw.example
  </footer>
</main>
</body>
</html>
```